Business Card Design
Brightvale Marks
Modern
Kemi Varo
47 Olumide Bankole Crescent
Wuse 2
Abuja
Nigeria
info@brightvalemarks.com
www.brightvalemarks.com

```html
<!DOCTYPE html>
<html lang="en">
<head>
<meta charset="utf-8">
<title>Brightvale Marks – Business Card</title>
<link href="https://fonts.googleapis.com/css2?family=Tinos:wght@400;700&display=swap" rel="stylesheet">
<style>
  :root {
    --stage: #e9eaec;
    --ink: #0b0b0b;
    --paper: #ffffff;
    --brand-blue: #1f86c6;
    --brand-green: #8cc63f;
    --text-light: #f2f2f2;
    --text-muted: #7a7a7a;
  }
  * { box-sizing: border-box; margin: 0; padding: 0; }
  html, body {
    width: 1200px; height: 901px; overflow: hidden;
    background: var(--stage);
    font-family: "Tinos", "Times New Roman", serif;
  }
  .canvas {
    position: relative; width: 1200px; height: 901px;
  }
  .card {
    position: absolute; left: 300px; width: 600px; height: 343px;
    overflow: hidden;
    box-shadow: 0 10px 28px rgba(0,0,0,.18);
  }
  /* Back side */
  .card--back { top: 60px; background: var(--ink); }
  .back-mark {
    position: absolute; left: 0; right: 0; top: 112px;
    display: flex; align-items: center; justify-content: center; gap: 14px;
  }
  .back-mark__dot {
    width: 46px; height: 46px; border-radius: 50%;
    background: var(--brand-blue);
  }
  .back-mark__name {
    color: var(--text-light); font-size: 30px; font-weight: 400;
    letter-spacing: 1px;
  }
  .back-url {
    position: absolute; left: 0; right: 0; top: 236px;
    text-align: center; color: var(--text-light); font-size: 16px;
  }
  /* Front side */
  .card--front { top: 478px; background: var(--paper); }
  .front-wave { position: absolute; inset: 0; }
  .front-logo {
    position: absolute; left: 28px; top: 96px;
    display: flex; align-items: center; gap: 10px;
  }
  .front-logo__dot {
    width: 30px; height: 30px; border-radius: 50%;
    background: var(--brand-green);
  }
  .front-logo__name {
    color: var(--brand-blue); font-size: 22px; font-weight: 400;
    letter-spacing: .5px;
  }
  .front-tagline {
    position: absolute; left: 68px; top: 130px;
    color: var(--text-muted); font-size: 8px; letter-spacing: .4px;
  }
  .contact {
    position: absolute; right: 30px; top: 44px;
    text-align: right; color: var(--text-light);
  }
  .contact__name { font-size: 22px; font-weight: 700; margin-bottom: 26px; }
  .contact__address { font-size: 15px; line-height: 1.35; margin-bottom: 22px; }
  .contact__line {
    display: flex; align-items: center; justify-content: flex-end; gap: 8px;
    font-size: 14px; line-height: 1.5;
  }
  .contact__icon { width: 12px; height: 12px; fill: var(--text-light); }
</style>
</head>
<body>
<main class="canvas">

  <section class="card card--back" aria-label="Card back">
    <div class="back-mark">
      <span class="back-mark__dot"></span>
      <span class="back-mark__name">Brightvale Marks</span>
    </div>
    <p class="back-url">www.brightvalemarks.com</p>
  </section>

  <section class="card card--front" aria-label="Card front">
    <svg class="front-wave" viewBox="0 0 600 343" preserveAspectRatio="none" aria-hidden="true">
      <path d="M300,0 L372,0 C338,40 346,110 300,180 C250,255 170,300 40,343 L0,343 L0,336 C150,300 238,250 276,170 C312,95 282,35 300,0 Z" fill="var(--brand-blue)"/>
      <path d="M382,0 L600,0 L600,343 L64,343 C200,305 282,250 322,170 C362,92 342,36 382,0 Z" fill="var(--ink)"/>
    </svg>

    <div class="front-logo">
      <span class="front-logo__dot"></span>
      <span class="front-logo__name">Brightvale Marks</span>
    </div>
    <p class="front-tagline">Building lasting value together always</p>

    <div class="contact">
      <p class="contact__name">Kemi Varo</p>
      <p class="contact__address">47 Olumide Bankole Crescent<br>Wuse 2 Abuja Nigeria</p>
      <p class="contact__line">08120004517
        <svg class="contact__icon" viewBox="0 0 12 12"><path d="M2.5 0.5l2 2.5-1.2 1.4c.7 1.6 1.8 2.7 3.3 3.4l1.4-1.2 2.5 2-1.3 2.4C5.2 11 1 6.8.5 1.8z"/></svg>
      </p>
      <p class="contact__line">info@brightvalemarks.com
        <svg class="contact__icon" viewBox="0 0 12 12"><path d="M0 2h12v8H0z M0 2l6 4.5L12 2" fill="none" stroke="currentColor" style="stroke:var(--text-light)" stroke-width="1.2"/></svg>
      </p>
      <p class="contact__line">www.brightvalemarks.com
        <svg class="contact__icon" viewBox="0 0 12 12"><circle cx="6" cy="6" r="5" fill="none" style="stroke:var(--text-light)" stroke-width="1.2"/><path d="M1 6h10M6 1v10" style="stroke:var(--text-light)" stroke-width="1"/></svg>
      </p>
    </div>
  </section>

</main>
</body>
</html>
```